Create Design/GRAPHICS/TEXT FOR VELKOR/E-COMMERCE PRODUCT

Hi,
I am looking for a designer to create a advertisement/images/text for a product that I sell on Velkor.
The first attachment is a 3d rendering of the product that I sell and want to use as the main image of the design.
The second attachment is of a existing ad on Velkor that you can use as a general idea of how I want the final graphic to look like.
The third and fourth attachments are of the text/graphics that I would like for you to include in the graphic.
Finally, the last attachment is my logo that I would like to include in the graphic.
Please feel free to get creative with this and if you have any questions please feel free to contact me.-
Update-I just added source files for logo as attachment six.
Thanks!
VELKOR
Product

```html
<!DOCTYPE html>
<html lang="en">
<head>
<meta charset="utf-8">
<title>Harlow BBQ Access Door</title>
<link rel="stylesheet" href="https://fonts.googleapis.com/css2?family=Source+Sans+3:wght@300;400;600&display=swap">
<style>
  :root {
    --page: #ffffff;
    --panel-top: #2b2c2e;
    --panel-bottom: #0e0f10;
    --band: #5b5d5f;
    --teal: #1a9c94;
    --text: #e6e6e6;
    --white: #ffffff;
    --label: #5d5f61;
    --steel-light: #c9cbcd;
    --steel-dark: #6d7073;
  }
  * { margin: 0; padding: 0; box-sizing: border-box; }
  html, body {
    width: 1200px; height: 1072px; overflow: hidden;
    background: var(--page);
    font-family: "Source Sans 3", sans-serif;
  }
  .ad-panel {
    position: absolute; left: 147px; top: 75px; width: 866px; height: 873px;
    background: linear-gradient(160deg, var(--panel-top), var(--panel-bottom));
    box-shadow: 0 8px 22px rgba(0,0,0,.35);
    overflow: hidden;
  }
  .product-glow {
    position: absolute; left: 283px; top: 165px; width: 583px; height: 465px;
    background: radial-gradient(ellipse at 55% 70%, rgba(110,112,115,.55), rgba(40,41,43,0) 70%);
  }
  .title-band {
    position: absolute; left: 0; top: 64px; width: 100%; height: 100px;
    background: var(--band);
  }
  .title {
    position: absolute; left: 75px; top: 17px;
    color: var(--white); font-weight: 400; font-size: 30px; line-height: 33px;
  }
  .brand {
    position: absolute; right: 42px; top: 24px; width: 150px;
    color: var(--white); font-weight: 400; text-align: center;
    font-size: 42px; line-height: 40px; letter-spacing: 1px;
  }
  .brand small { display: block; font-size: 13px; line-height: 18px; letter-spacing: 2px; }
  .product-render {
    position: absolute; left: 410px; top: 232px; width: 420px; height: 340px;
    background: linear-gradient(120deg, var(--steel-light), var(--steel-dark) 60%, #3a3c3e);
    border-radius: 4px; opacity: .9;
  }
  .feature {
    position: absolute; left: 117px; color: var(--text);
    font-size: 15.5px; line-height: 22px; font-weight: 400;
  }
  .tick { position: absolute; left: -20px; top: 5px; width: 15px; height: 15px; }
  .leaders { position: absolute; left: 0; top: 0; }
  .value-row { position: absolute; left: 41px; top: 637px; }
  .value-card {
    position: absolute; top: 0; width: 129px; height: 181px;
    border: 2px solid var(--teal); text-align: center; color: var(--white);
  }
  .value-card .face { height: 114px; display: flex; flex-direction: column; justify-content: center; align-items: center; }
  .seal { width: 96px; height: 96px; border: 4px solid var(--white); border-radius: 50%; display: flex; align-items: center; justify-content: center; }
  .seal span { width: 62px; height: 62px; border: 2px solid var(--white); border-radius: 50%; display: block; }
  .label {
    background: var(--label); height: 20px; font-size: 12.5px; line-height: 20px; font-weight: 600;
  }
  .note { font-size: 9.5px; line-height: 12px; padding: 6px 6px 0; }
  .face.big { font-size: 18px; line-height: 22px; }
  .face.mid { font-size: 14px; line-height: 18px; }
  .face .num { font-size: 20px; line-height: 26px; font-weight: 400; }
</style>
</head>
<body>
<div class="ad-panel">
  <div class="product-glow"></div>

  <div class="title-band">
    <h1 class="title">Hand Crafted BBQ access door<br>Elegant Design With Double Construction</h1>
    <div class="brand">HARLOW<small>outdoor kitchens</small></div>
  </div>

  <div class="product-render" role="img" aria-label="3D render of an open stainless steel BBQ access door with paper towel holder and vertical handle"></div>

  <svg class="leaders" width="866" height="873" viewBox="0 0 866 873" fill="none" stroke="#1a9c94" stroke-width="1">
    <polyline points="384,234 444,234 444,261"/>
    <polyline points="382,301 543,301"/>
    <polyline points="384,432 429,432 429,473"/>
    <polyline points="384,492 823,492 823,453"/>
    <polyline points="384,545 493,545 493,388"/>
    <g fill="#1a9c94" stroke="none">
      <circle cx="444" cy="261" r="4"/>
      <circle cx="543" cy="301" r="4"/>
      <circle cx="429" cy="473" r="4"/>
      <circle cx="823" cy="453" r="4"/>
      <circle cx="493" cy="388" r="4"/>
    </g>
  </svg>

  <p class="feature" style="top:220px"><svg class="tick" viewBox="0 0 15 15"><path d="M1 8l4 5L14 1" stroke="#1a9c94" stroke-width="1.4" fill="none"/></svg>Premium 304 stainless steel<br>construction</p>
  <p class="feature" style="top:286px"><svg class="tick" viewBox="0 0 15 15"><path d="M1 8l4 5L14 1" stroke="#1a9c94" stroke-width="1.4" fill="none"/></svg>Rugged 16&nbsp; guage frame construction</p>
  <p class="feature" style="top:330px">Double wall construction<br>- 19 guage outer wall<br>- 70 guage inner wall</p>
  <p class="feature" style="top:417px"><svg class="tick" viewBox="0 0 15 15"><path d="M1 8l4 5L14 1" stroke="#1a9c94" stroke-width="1.4" fill="none"/></svg>Secure 4 point magnet closing system</p>
  <p class="feature" style="top:461px"><svg class="tick" viewBox="0 0 15 15"><path d="M1 8l4 5L14 1" stroke="#1a9c94" stroke-width="1.4" fill="none"/></svg>High Quality 304 grade stainless steel<br>handle</p>
  <p class="feature" style="top:526px"><svg class="tick" viewBox="0 0 15 15"><path d="M1 8l4 5L14 1" stroke="#1a9c94" stroke-width="1.4" fill="none"/></svg>Convenient paper towel holder</p>

  <div class="value-row">
    <div class="value-card" style="left:0">
      <div class="face"><div class="seal"><span></span></div></div>
      <div class="label">QUALITY</div>
      <p class="note">Our employers take pride in their work</p>
    </div>
    <div class="value-card" style="left:158px">
      <div class="face big">Double<br>Wall<br>Construction</div>
      <div class="label">VALUE</div>
      <p class="note">Our doors weight 10pounds more than the competition</p>
    </div>
    <div class="value-card" style="left:316px">
      <div class="face mid">Premium Grade<br><span class="num">304</span><br>Stainless Steel</div>
      <div class="label">STRENGTH</div>
      <p class="note">Offers higher level of corrosion resistance</p>
    </div>
    <div class="value-card" style="left:474px">
      <div class="face mid"><span class="num">16 G</span>frame<br><span class="num" style="margin-top:8px">18 G</span>outer wall</div>
      <div class="label">DURABILITY</div>
      <p class="note">Thick and durable stainless steel construction</p>
    </div>
    <div class="value-card" style="left:632px">
      <div class="face"><div class="seal"><span></span></div></div>
      <div class="label">PEACE OF MIND</div>
      <p class="note">Your satisfaction is our highest goal</p>
    </div>
  </div>
</div>
</body>
</html>
```